Harrowgate Legal

To update and modernize current business card appearance. Marisa's business is based in Melbourne with 4 other lawyers in the firm. Marisa travels to the Pilbara in Western Australia approximately 1 week a month as part of the firms legal work. She consults with clients in Newman, Tom Price and Port Hedland. The lawyers work mostly from a home office, apart from court appearances. They have a virtual office in Melbourne city, and use facilities in 3 or 4 other locations around Melbourne. It is important the client's think this is a conventional law firm with a permanent office. Our business structure is a difficult concept for them to grasp. The business has been operational for 3 years, growing from 1 lawyer to 4 lawyers during that time. Our website is www.Harrowgatelegal.com.au and is currently being upgraded as we are not happy with its content. The logo is currently orange and dark grey but the orange is a difficult colour to reproduce and often turns out "poo" brown when documents are printed. We need clients to know we are user friendly and caring - and not head up our rears ends as some lawyers appear to be.
Updates

Thank you for the feedback so far. 1. Some of the designs have too much black (We prefer darker grey & not too much.) 2. Happy for designers to play around with different colours & logo design. What we're after is a modern look and business card that people say "wow" when they pick it up.

Industry/Entity Type

Business

```html
<!DOCTYPE html>
<html lang="en">
<head>
<meta charset="utf-8">
<title>Harrowgate Legal – Business Card</title>
<link rel="stylesheet" href="https://fonts.googleapis.com/css2?family=Poppins:wght@400;600&display=swap">
<style>
  :root {
    --page: #ecebe8;
    --card: #ffffff;
    --ink: #222222;
    --grey: #4a4a4c;
    --red: #e1222b;
    --red-tint: #fde9ea;
    --shadow: rgba(0, 0, 0, 0.18);
  }
  * { box-sizing: border-box; margin: 0; padding: 0; }
  html, body {
    width: 1200px;
    height: 1000px;
    overflow: hidden;
    background: var(--page);
    font-family: "Poppins", sans-serif;
    color: var(--ink);
  }
  .canvas {
    position: relative;
    width: 1200px;
    height: 1000px;
  }
  .card {
    position: absolute;
    left: 280px;
    width: 640px;
    height: 366px;
    background: var(--card);
    border-radius: 10px;
    box-shadow: 0 8px 24px var(--shadow);
    overflow: hidden;
  }
  .card--back { top: 70px; }
  .card--front { top: 520px; }

  /* Back of card */
  .pattern-area {
    position: absolute;
    inset: 0;
    background: linear-gradient(135deg, var(--red-tint) 0%, var(--card) 45%, var(--card) 55%, var(--red-tint) 100%);
  }
  .brand {
    position: absolute;
    display: flex;
    align-items: center;
    gap: 14px;
    color: var(--grey);
    font-weight: 400;
    white-space: nowrap;
  }
  .brand__dot {
    flex: none;
    border-radius: 50%;
    background: var(--red);
  }
  .card--back .brand {
    left: 50%;
    top: 50%;
    transform: translate(-50%, -50%);
    font-size: 44px;
    letter-spacing: 1px;
  }
  .card--back .brand__dot { width: 30px; height: 30px; }

  /* Front of card */
  .holder {
    position: absolute;
    left: 44px;
    top: 40px;
  }
  .holder__name {
    font-size: 34px;
    font-weight: 600;
    line-height: 1.1;
    letter-spacing: -0.3px;
  }
  .holder__creds {
    margin-top: 8px;
    margin-left: 8px;
    font-size: 11px;
  }
  .holder__role {
    margin-top: 4px;
    margin-left: 8px;
    font-size: 16px;
  }
  .contact {
    list-style: none;
    margin-top: 14px;
    margin-left: 8px;
    font-size: 12px;
    line-height: 1.55;
  }
  .card--front .brand {
    right: 36px;
    top: 196px;
    font-size: 24px;
    gap: 10px;
  }
  .card--front .brand__dot { width: 16px; height: 16px; }
  .region {
    position: absolute;
    left: 44px;
    bottom: 40px;
    font-size: 23px;
    font-weight: 600;
  }
</style>
</head>
<body>
<main class="canvas">
  <section class="card card--back">
    <div class="pattern-area" role="img" aria-label="Red decorative ring pattern across the card back"></div>
    <div class="brand">
      <span class="brand__dot"></span>
      <span class="brand__name">Harrowgate Legal</span>
    </div>
  </section>

  <section class="card card--front">
    <div class="holder">
      <h1 class="holder__name">J. Marisa Thornbury</h1>
      <p class="holder__creds">LLB (Hons) - Accredited Mediator</p>
      <p class="holder__role">Principal Solicitor</p>
      <ul class="contact">
        <li>1300 Harrowgate (427 746)</li>
        <li>0400 555 018</li>
        <li>marisa.thornbury@harrowgatelegal.com.au</li>
      </ul>
    </div>
    <div class="brand">
      <span class="brand__dot"></span>
      <span class="brand__name">Harrowgate Legal</span>
    </div>
    <p class="region">Melbourne Eastern And Bayside Suburbs</p>
  </section>
</main>
</body>
</html>
```